Coastwell Keys Agency Guarantee

We need a flyer to promote a Sydney based property management agency.
We specialise in Property Management on the Northern Beaches of Sydney. A small boutique agency that prides itself on high quality customer service and the lowest fees.
We would like this flyer to promote our listed features in the document provided and focus on our money back guarantee.
The flyer must:
- be designed to match our website www.coastwellkeysagency.com.au
- Contain our logo and contact details
- Use the attached photoshop template for bleed, sizing and fold lines
- final files must include a print ready PDF and fully editable PSD (photoshop) file with included fonts.
Attached are the following files:
Contact details are:
Name: Tom Farrow
Tel: 0491 527 068
email: tom@coastwellkeysagency.com.au
Office: Level 2, 17 Tennerby Rd, Fernhaven NSW 2107
Web: www.coastwellkeysagency.com.au
Target Market(s)
35-75yo Male and Females that own investment properties on Sydney's Norther Beaches
Industry/Entity Type
Real Estate
Requirements
Must have
- The flyer must:
- - Be double sided and colour
- - be designed to match our website www.coastwellkeysagency.com.au
- - Contain our logo and contact details
- - Use the attached photoshop template for bleed, sizing and fold lines
- - final files must include a print ready PDF and fully editable PSD (photoshop) file with included fonts.
Nice to have
- A Money back guarantee "stamp"

```html
<!DOCTYPE html>
<html lang="en">
<head>
<meta charset="utf-8">
<title>Coastwell Keys Agency – Property Management Trifold</title>
<link rel="stylesheet" href="https://fonts.googleapis.com/css2?family=Oswald:wght@300;500;600&family=Open+Sans:ital,wght@0,400;0,600;0,700;1,700&display=swap">
<style>
  :root {
    --teal: #34b4c2;
    --teal-dark: #1f8f9c;
    --grey: #64686b;
    --grey-dark: #4b4e51;
    --grey-light: #d9dcde;
    --ink: #5a5e61;
    --paper: #ffffff;
    --backdrop: #eceef0;
  }
  * { box-sizing: border-box; margin: 0; padding: 0; }
  html, body { width: 1200px; height: 990px; overflow: hidden; }
  body {
    background: var(--backdrop);
    font-family: "Open Sans", Arial, sans-serif;
    color: var(--ink);
  }
  .trifold {
    position: absolute; left: 30px; top: 92px;
    width: 1140px; height: 806px;
    display: flex; background: var(--paper);
    box-shadow: 0 6px 24px rgba(0,0,0,.15);
  }
  .panel { position: relative; width: 380px; height: 806px; overflow: hidden; }
  .panel + .panel { border-left: 1px solid #eef0f1; }
  .panel-shapes { position: absolute; inset: 0; width: 380px; height: 806px; }
  .block { position: absolute; left: 30px; right: 28px; }

  /* Inside-left panel */
  .section-title { color: var(--teal-dark); font-weight: 700; font-size: 16px; line-height: 1.25; }
  .body-copy { font-size: 11px; line-height: 1.5; margin-top: 8px; }
  .panel-guarantee .guarantee-copy .body-copy { line-height: 1.4; margin-top: 6px; }
  .guarantee-title {
    position: absolute; left: 30px; top: 249px;
    color: #fff; font-weight: 700; font-size: 21px;
    transform: rotate(-3deg); transform-origin: left;
  }
  .fine-print { font-size: 11px; line-height: 1.35; font-weight: 700; font-style: italic; color: var(--teal-dark); margin-top: 8px; }
  .room-photo {
    position: absolute; left: 24px; top: 658px; width: 96px; height: 96px;
    border-radius: 50%; border: 4px solid #fff;
    background: radial-gradient(circle at 40% 40%, #e8eef0, #9fb6bb 70%, #6f8a8f);
    box-shadow: 0 2px 6px rgba(0,0,0,.2);
  }
  .guarantee-stamp {
    position: absolute; left: 100px; top: 672px; width: 52px; height: 52px;
    border-radius: 50%; background: #7fb85a; border: 3px solid #fff;
  }
  .web-address {
    position: absolute; left: 0; right: 0; bottom: 26px;
    color: #fff; font-weight: 700; font-size: 14px; text-align: center;
  }

  /* Middle panel */
  .team-title { font-weight: 700; font-size: 25px; color: var(--grey-dark); }
  .watermark-name {
    position: absolute; left: 0; right: 0; top: 290px; text-align: center;
    font-family: "Oswald", "Arial Narrow", sans-serif; font-weight: 500;
    font-size: 20px; letter-spacing: 1px; color: #e4e6e8; text-transform: uppercase;
  }
  .portrait-photo {
    position: absolute; left: 30px; top: 330px; width: 170px; height: 318px;
    border-radius: 85px 85px 0 0;
    background: linear-gradient(180deg, #c9d3df 0%, #8fa6c2 55%, #6f88a8 100%);
  }
  .contact-name {
    position: absolute; right: 30px; top: 590px;
    color: var(--teal-dark); font-weight: 700; font-size: 20px;
  }
  .contact-list {
    position: absolute; left: 30px; top: 688px; list-style: none;
    color: #fff; font-size: 11.5px; line-height: 1.35;
  }
  .contact-list li { display: flex; align-items: flex-start; gap: 10px; margin-bottom: 5px; }
  .contact-list svg { flex: none; width: 13px; height: 13px; margin-top: 1px; }

  /* Cover panel */
  .brand-name {
    position: absolute; left: 0; right: 0; top: 62px; text-align: center;
    color: #fff; font-weight: 600; font-size: 23px; letter-spacing: 1px;
  }
  .homes-photo {
    position: absolute; left: 0; top: 110px; width: 380px; height: 330px;
    background: linear-gradient(180deg, #bfe1f0 0%, #e9f1f3 30%, #8fae84 60%, #4f7b4a 100%);
  }
  .headline {
    position: absolute; right: 28px; top: 488px; text-align: right;
    font-family: "Oswald", "Arial Narrow", sans-serif; text-transform: uppercase; line-height: 1;
  }
  .headline .line-1 { display: block; font-weight: 600; font-size: 66px; color: var(--grey-dark); }
  .headline .line-2 { display: block; font-weight: 600; font-size: 45px; color: var(--teal-dark); margin-top: 4px; }
  .headline .line-3 { display: block; font-weight: 300; font-size: 50px; color: var(--grey-dark); margin-top: 4px; }
</style>
</head>
<body>
<main class="trifold">

  <section class="panel panel-guarantee">
    <svg class="panel-shapes" viewBox="0 0 380 806" aria-hidden="true">
      <polygon points="0,0 160,0 0,16" fill="var(--teal)"/>
      <polygon points="0,246 380,224 380,266 0,290" fill="var(--teal)"/>
      <path d="M0,700 Q190,660 380,690 L380,806 L0,806 Z" fill="var(--grey)"/>
      <path d="M0,722 Q190,684 380,712 L380,806 L0,806 Z" fill="var(--teal)"/>
    </svg>
    <div class="block" style="top:28px">
      <h2 class="section-title">What Separates Coastwell Keys Agency:</h2>
      <p class="body-copy">Coastwell Keys Agency is a boutique agency that specialises in Property Management. We differ from your typical agency because our primary business is property management. You will have a senior property manager that is solely focused on maximising your investment's potential. As property investors ourselves we understand the frustrations you have with a typical agency, and we promise to offer you the service, care and professionalism beyond what you expect. Guaranteed!</p>
    </div>
    <h2 class="guarantee-title">Our Guarantee:</h2>
    <div class="block guarantee-copy" style="top:298px">
      <p class="body-copy">At Coastwell Keys Agency we are the Risk Reduction Specialists! Our team will work with you to ensure you're receiving the highest possible return on your investment property. The entire department is heavily focused on maximising your income and optimising capital growth on your investment property.</p>
      <p class="body-copy">We understand when you are selecting a new managing agent it can be a very stressful process for many landlords as you don't know if they are going to deliver on their promises. At Coastwell Keys Agency we understand promises can be easily broken and the good news is we GUARANTEE our service.</p>
      <p class="body-copy">If during the first 3 months you are not satisfied with our level of service we promise to you, we are prepared to refund the first 3 months and will give 100% money back on your management fees*</p>
      <p class="fine-print">* Only applies to management fees. Coastwell Keys Agency must be notified in writing within the 3 month service guarantee period.</p>
    </div>
    <div class="room-photo" role="img" aria-label="Photo of a bright furnished bedroom"></div>
    <div class="guarantee-stamp" role="img" aria-label="Money back guarantee stamp"></div>
    <p class="web-address">www.coastwellkeysagency.com.au</p>
  </section>

  <section class="panel panel-team">
    <svg class="panel-shapes" viewBox="0 0 380 806" aria-hidden="true">
      <polygon points="0,0 380,0 380,30 0,62" fill="var(--grey)"/>
      <polygon points="0,62 380,30 380,38 0,70" fill="var(--grey-light)"/>
      <path d="M0,650 L380,618 L380,806 L0,806 Z" fill="var(--grey-light)"/>
      <path d="M0,664 L380,632 L380,806 L0,806 Z" fill="var(--grey-dark)"/>
    </svg>
    <div class="block" style="top:92px">
      <h2 class="team-title">Our broad team:</h2>
      <p class="body-copy">Not only do we have a friendly, professional and efficient property management team - we also work closely with associated builders, accountants and mortgage brokers. So you have access to experienced professionals in all facets of property investment.</p>
      <p class="body-copy">We work for you and it's in our best interest that you get the best advice and service possible to get the most out of your investment.</p>
    </div>
    <p class="watermark-name">Coastwell Keys</p>
    <div class="portrait-photo" role="img" aria-label="Portrait photo of agency principal Tom Farrow in a blue shirt, arms folded"></div>
    <p class="contact-name">Tom Farrow</p>
    <ul class="contact-list">
      <li>
        <svg viewBox="0 0 12 12"><path d="M6 0.5a4 4 0 0 1 4 4c0 3-4 7-4 7s-4-4-4-7a4 4 0 0 1 4-4z" fill="#fff"/><circle cx="6" cy="4.5" r="1.5" fill="var(--grey-dark)"/></svg>
        <span>Level 2, 17 Tennerby Rd, Fernhaven<br>NSW 2107</span>
      </li>
      <li>
        <svg viewBox="0 0 12 12"><path d="M2.5 1h2l1 2.5-1.3 1a6 6 0 0 0 3.3 3.3l1-1.3 2.5 1v2a1 1 0 0 1-1 1A9.5 9.5 0 0 1 1.5 2a1 1 0 0 1 1-1z" fill="#fff"/></svg>
        <span>0491 527 068</span>
      </li>
      <li>
        <svg viewBox="0 0 12 12"><rect x="0.5" y="2" width="11" height="8" fill="#fff"/><path d="M0.5 2.5l5.5 4 5.5-4" stroke="var(--grey-dark)" fill="none"/></svg>
        <span>tom@coastwellkeysagency.com.au</span>
      </li>
      <li>
        <svg viewBox="0 0 12 12"><circle cx="6" cy="6" r="5" fill="none" stroke="#fff"/><path d="M1 6h10M6 1c-2.5 3-2.5 7 0 10M6 1c2.5 3 2.5 7 0 10" stroke="#fff" fill="none"/></svg>
        <span>www.coastwellkeysagency.com.au</span>
      </li>
    </ul>
  </section>

  <section class="panel panel-cover">
    <div class="homes-photo" role="img" aria-label="Photo of modern terraced coastal homes with landscaped gardens"></div>
    <svg class="panel-shapes" viewBox="0 0 380 806" aria-hidden="true">
      <path d="M0,0 L380,0 L380,110 L250,160 L0,112 Z" fill="var(--teal)"/>
      <path d="M0,112 L250,160 L380,110 L380,118 L250,168 L0,120 Z" fill="var(--grey)"/>
      <polygon points="0,440 380,410 380,806 0,806" fill="var(--paper)"/>
      <polygon points="0,430 380,400 380,418 0,448" fill="var(--grey)"/>
      <polygon points="0,742 380,706 380,806 0,806" fill="var(--teal)"/>
      <polygon points="0,734 380,698 380,706 0,742" fill="var(--grey)"/>
    </svg>
    <p class="brand-name">Coastwell Keys Agency</p>
    <h1 class="headline">
      <span class="line-1">Property</span>
      <span class="line-2">Management</span>
      <span class="line-3">Done Right!</span>
    </h1>
    <p class="web-address">www.coastwellkeysagency.com.au</p>
  </section>

</main>
</body>
</html>
```